Flooring Company Stationery Design Project

I need Business card, presentation folder, letterhead and envelope design.
I want the design to show a lot of creativity and that it has a modern look but still professional.
The company has a retail store but we specialize in in-home shopping.

Design must have a "flooring" company style. Creativity is going to be the main thing we'll be looking for. We want something that will stand out of the competition.

We are a remodeling busines and we want to look like one but with a good look.

PLEASE USE FOLLOWING LINK FOR ANY PHOTOS NEEDED
http://www.velmorta.com/syndicate/logos/choose_brands.html
Updates

PLEASE USE ANY PHOTOS NEEDED FROM HERE

Target Market(s)

Our target customer are 35-50 years old and decision makers are usually women

Industry/Entity Type

Retail

Requirements
Must have
• Color red
PHOTOS NEEDED CAN BE USED FROM HERE

```html
<!DOCTYPE html>
<html lang="en">
<head>
<meta charset="utf-8">
<title>Plankwell – Business Card</title>
<link rel="stylesheet" href="https://fonts.googleapis.com/css2?family=Lato:wght@400;700;900&display=swap">
<style>
  :root {
    --page-bg: #e6e9eb;
    --card-white: #ffffff;
    --card-dark: #2c2c2c;
    --band-dark: #333333;
    --brand-red: #d3191c;
    --ink: #222222;
    --ink-soft: #3a3a3a;
    --on-dark: #ffffff;
  }
  * { box-sizing: border-box; margin: 0; padding: 0; }
  html, body {
    width: 1200px; height: 960px; overflow: hidden;
    background: var(--page-bg);
    font-family: "Lato", Arial, sans-serif;
  }
  .stationery {
    width: 1200px; height: 960px;
    display: flex; flex-direction: column;
    align-items: center; justify-content: center; gap: 56px;
  }
  .card {
    width: 700px; height: 400px; position: relative;
    box-shadow: 0 12px 30px rgba(0,0,0,.18);
  }
  .card--front { background: var(--card-white); }
  .card--back {
    background: var(--card-dark);
    display: flex; align-items: center; justify-content: center;
  }
  .brand-name {
    font-weight: 900; color: var(--brand-red);
    letter-spacing: -1px; line-height: 1;
  }
  .card--front .brand-name {
    position: absolute; left: 40px; top: 58px; font-size: 64px;
  }
  .card--back .brand-name { font-size: 62px; }
  .name-band {
    position: absolute; left: 0; right: 0; top: 176px; height: 58px;
    background: var(--band-dark); color: var(--on-dark);
    display: flex; align-items: center; padding-left: 40px;
  }
  .name-band .person { font-size: 30px; font-weight: 400; }
  .name-band .role {
    font-size: 17px; text-transform: uppercase; letter-spacing: .5px;
    margin-left: 8px; margin-top: 6px;
  }
  .contacts {
    position: absolute; left: 40px; bottom: 38px;
    list-style: none; color: var(--ink); font-size: 21px;
  }
  .contacts li { display: flex; align-items: center; gap: 14px; line-height: 32px; }
  .contacts svg { width: 18px; height: 18px; flex: none; }
  .address {
    position: absolute; right: 40px; top: 262px;
    font-size: 17px; line-height: 25px; color: var(--ink-soft);
    font-style: normal;
  }
  .address .web { font-weight: 700; color: var(--ink); }
</style>
</head>
<body>
<main class="stationery">
  <section class="card card--front" aria-label="Business card front">
    <div class="brand-name">plankwell</div>
    <div class="name-band">
      <span class="person">Dana Whitlock</span>
      <span class="role">/ Operation Manager</span>
    </div>
    <ul class="contacts">
      <li>
        <svg viewBox="0 0 24 24" aria-hidden="true"><path fill="#222" d="M6.6 10.8a15 15 0 0 0 6.6 6.6l2.2-2.2a1 1 0 0 1 1-.25 11.4 11.4 0 0 0 3.6.57 1 1 0 0 1 1 1V20a1 1 0 0 1-1 1A17 17 0 0 1 3 4a1 1 0 0 1 1-1h3.5a1 1 0 0 1 1 1c0 1.25.2 2.45.57 3.57a1 1 0 0 1-.25 1z"/></svg>
        +1 416 555 0142
      </li>
      <li>
        <svg viewBox="0 0 24 24" aria-hidden="true"><rect x="6" y="2" width="12" height="20" rx="2" fill="none" stroke="#222" stroke-width="2"/><rect x="9" y="5" width="6" height="6" fill="#222"/><circle cx="12" cy="17" r="1.5" fill="#222"/></svg>
        +1 416 555 0187
      </li>
      <li>
        <svg viewBox="0 0 24 24" aria-hidden="true"><rect x="2" y="5" width="20" height="14" fill="none" stroke="#222" stroke-width="2"/><path d="M2 5l10 8 10-8M2 19l7-7M22 19l-7-7" fill="none" stroke="#222" stroke-width="2"/></svg>
        name@plankwell.com
      </li>
    </ul>
    <address class="address">
      48 Harbour Lane,<br>
      Toronto, Ontario M4K 2B9<br>
      <span class="web">www.plankwell.com</span>
    </address>
  </section>

  <section class="card card--back" aria-label="Business card back">
    <div class="brand-name">plankwell</div>
  </section>
</main>
</body>
</html>
```